redesing professional certificate

Redesign our certificate to more a professional look and to make it look like a-wanna have - Best in adobe photoshop, because this template will be our basic, and we have in our education different levels, basic, upper, lower, complex, master level. I usually add a small picture to show what level they are. Or when you have a better suggestion I a gladly to hear.
We teach to physiotherapist so it has to look professional.

Target Market(s)

physiotherapist

Industry/Entity Type

Health Care

Requirements
Must have
• our logo

```html
<!DOCTYPE html>
<html lang="en">
<head>
<meta charset="utf-8">
<title>Certificate of Training</title>
<link rel="stylesheet" href="https://fonts.googleapis.com/css2?family=Playfair+Display:wght@700&family=Arimo:ital,wght@0,400;0,700;1,400&display=swap">
<style>
  :root {
    --navy: #1b2443;
    --navy-deep: #16304a;
    --amber: #f8a510;
    --coral: #f2967a;
    --ink: #111111;
    --paper: #ffffff;
  }
  * { margin: 0; padding: 0; box-sizing: border-box; }
  html, body { width: 1200px; height: 900px; overflow: hidden; background: var(--paper); }
  body { font-family: "Arimo", Arial, sans-serif; color: var(--ink); }

  .certificate { position: relative; width: 1200px; height: 900px; background: var(--paper); }

  .side-band {
    position: absolute; left: 0; top: 0; width: 210px; height: 900px;
    background: linear-gradient(180deg, #1b2443 0%, #2a3458 50%, #1b2443 100%);
  }

  .frame {
    position: absolute; left: 238px; top: 29px; right: 27px; bottom: 22px;
    border: 3px solid var(--coral);
  }

  .centered { position: absolute; left: 238px; right: 27px; text-align: center; }

  .title {
    top: 62px; font-family: "Playfair Display", Georgia, serif; font-weight: 700;
    font-size: 74px; color: var(--amber); letter-spacing: 0.5px; line-height: 1;
  }
  .intro { top: 178px; font-size: 21px; }
  .recipient { top: 212px; font-size: 36px; font-weight: 700; color: var(--navy); }
  .course { top: 260px; font-size: 21px; line-height: 28px; }
  .course .course-name { font-size: 25px; }

  .signature { position: absolute; top: 450px; width: 200px; border-top: 2px solid var(--navy); }
  .signature--left { left: 419px; }
  .signature--right { left: 745px; text-align: right; top: 450px; }
  .signature-name { font-size: 22px; color: var(--navy); padding-top: 8px; }
  .signature--right .signature-name { padding-top: 3px; }
  .signature-role { font-size: 17px; font-style: italic; color: var(--navy); }

  .registration { top: 546px; font-size: 19px; }
  .notice { top: 595px; font-size: 19px; line-height: 25px; }

  .issuer-mark {
    position: absolute; left: 412px; top: 710px; width: 130px; height: 130px;
    border-radius: 50%; background: var(--navy); border: 3px solid #d9dde6;
    box-shadow: 0 0 0 1px var(--navy);
  }
  .issuer { position: absolute; left: 585px; top: 718px; }
  .issuer-name { font-size: 27px; line-height: 32px; }
  .issuer-address { font-size: 19px; line-height: 25px; }
  .issuer-tagline {
    position: absolute; left: 581px; top: 804px; width: 374px; height: 31px;
    background: var(--navy-deep); color: var(--paper); font-size: 19px;
    line-height: 31px; text-align: center;
  }
</style>
</head>
<body>
<main class="certificate">
  <div class="side-band" role="img" aria-label="Decorative band of flowing fine wave lines on navy"></div>
  <div class="frame"></div>

  <h1 class="centered title">Certificate of Training</h1>
  <p class="centered intro">This is to certify that</p>
  <p class="centered recipient">Tomas Avelar</p>
  <p class="centered course">has completed the course <span class="course-name">Fasciatherapy level I</span><br>undertaken on 15th-17th February 2020<br>at Kopavogur, Iceland</p>

  <div class="signature signature--left">
    <p class="signature-name">Mr JM van Rooden</p>
    <p class="signature-role">Co-Director</p>
  </div>
  <div class="signature signature--right">
    <p class="signature-name">Mr DK Harlow</p>
    <p class="signature-role">Co-Director</p>
  </div>

  <p class="centered registration">Registration number: 7 ICE 20</p>
  <p class="centered notice">The Myofascial Balance Method ongoing certification is<br>contingent upon meeting the requirements of maintenance<br>of the certification of Fasciatherapy.</p>

  <div class="issuer-mark"></div>
  <div class="issuer">
    <p class="issuer-name">Corvelle Fascia Academy BV</p>
    <p class="issuer-address">Tweede Lindengracht 48<br>1015KD Amsterdam, The Netherlands</p>
  </div>
  <p class="issuer-tagline">Specialists in Fasciatherapy Innovation</p>
</main>
</body>
</html>
```